Brightwave Cellular Landing Page

The goal of this landing page to encourage viewers to either download the Orbix or Zphone APP, Follow us on a Social Network Medium, Switch to Brightwave Cellular Prepaid Wireless Plan or Purchase additional Usage (No contracts), and/or Sign up as a Reseller / Distributor. The viewer must feel inclined to do something of the sort if they have any interest in Brightwave Cellular. The calls to action are listed in the Must Have section

Target Market(s)

Prepaid wireless market, no contracts, bring your own phone, unlimited plans, zenocell network, 4G network, no credit check

Industry/Entity Type

Orbix

Requirements
Must have
• The Landing page must contain the following elements:
1) Brightwave Cellular logo: (see example: http://www.mybrightwavecellular.example) The logo on the website
2) Brightwave Cellular Current Promotion (see example: http://www.mybrightwavecellular.example/Brightwave-Cellular-Plan.aspx)
3) Image Link to download our own Brightwave Cellular Zphone & Orbix APP (call to action)
4) Image Link to Follow our Brightwave Cellular Chatterloop & Peepstream page (call to action)
5) Image Link to Reseller / Distributor Opportunities to earn commissions (call to action)
6) uTalkCredits.example Logo: (see example: http://www.utalkcredits.example) The logo on the website
Should not have
• Be a standard webpage with information, this is a landing page, a call to action, they must click

```html
<!DOCTYPE html>
<html lang="en">
<head>
<meta charset="utf-8">
<title>uTalkCredits – Monthly Plans</title>
<link href="https://fonts.googleapis.com/css2?family=Roboto:wght@300;400;500;900&display=swap" rel="stylesheet">
<style>
  :root {
    --green: #8cc63f;
    --green-dark: #5e9e25;
    --tab-top: #8fcd4a;
    --tab-bottom: #5e9e25;
    --white: #ffffff;
    --grey-text: #808080;
    --footer-text: #9a9a9a;
    --app-blue: #2f7db2;
    --chat-blue: #3b5a98;
    --peep-blue: #3aa2d8;
    --price-shade: #c9ccd0;
  }
  * { margin: 0; padding: 0; box-sizing: border-box; }
  html, body { width: 1200px; height: 900px; overflow: hidden; background: var(--white); }
  body { position: relative; font-family: "Roboto", Arial, sans-serif; }

  .lang-switch { position: absolute; top: 0; left: 968px; display: flex; gap: 6px; }
  .lang-switch a {
    display: block; height: 40px; line-height: 40px; text-align: center;
    border: 1.5px solid var(--green); border-top: none; border-radius: 0 0 6px 6px;
    color: var(--green); font-size: 14px; text-decoration: none;
  }
  .lang-en { width: 106px; }
  .lang-es { width: 120px; }

  .quick-links { position: absolute; left: 20px; top: 47px; list-style: none; }
  .quick-links li { font-size: 17px; line-height: 21.5px; color: var(--grey-text); font-weight: 300; }

  .brand { position: absolute; left: 366px; top: 50px; width: 470px; text-align: right; }
  .brand-name { display: flex; align-items: center; gap: 12px; font-size: 64px; font-weight: 500; color: var(--green); letter-spacing: -1px; line-height: 1; }
  .brand-dot { width: 26px; height: 26px; border-radius: 50%; background: var(--green); flex: none; }
  .brand-tagline { font-size: 15px; color: var(--grey-text); margin-top: 2px; }

  .carrier-brand { position: absolute; left: 968px; top: 78px; width: 232px; display: flex; align-items: center; gap: 8px; font-size: 19px; font-weight: 500; color: var(--green-dark); }
  .carrier-mark { width: 14px; height: 14px; background: var(--green-dark); flex: none; }

  .main-nav { position: absolute; top: 189px; left: 159px; display: flex; gap: 6px; }
  .main-nav a {
    width: 105px; height: 42px; line-height: 42px; text-align: center;
    background: linear-gradient(var(--tab-top), var(--tab-bottom));
    border-radius: 5px 5px 0 0; color: var(--white); font-size: 15px; font-weight: 300; text-decoration: none;
  }

  .promo { position: absolute; top: 231px; left: 0; width: 1200px; height: 621px; background: var(--green); }

  .sidebar { position: absolute; left: 0; top: 0; width: 170px; text-align: center; color: var(--white); }
  .sidebar-title { position: absolute; width: 170px; font-size: 14px; font-weight: 300; }
  .title-apps { top: 50px; }
  .title-follow { top: 427px; }
  .app-link {
    position: absolute; left: 27px; width: 116px; height: 115px; display: flex; align-items: center; justify-content: center;
    font-size: 22px; font-weight: 500; text-decoration: none;
  }
  .app-zphone { top: 81px; background: var(--white); color: var(--grey-text); }
  .app-orbix { top: 221px; background: var(--app-blue); color: var(--white); }
  .social-link {
    position: absolute; left: 62px; width: 48px; height: 47px; border-radius: 4px; display: flex; align-items: center; justify-content: center;
    font-size: 8px; color: var(--white); text-decoration: none;
  }
  .social-chatterloop { top: 464px; background: var(--chat-blue); }
  .social-peepstream { top: 537px; background: var(--peep-blue); }

  .divider { position: absolute; left: 160px; top: 21px; width: 1.5px; height: 573px; background: var(--white); opacity: .85; }

  .plans-title { position: absolute; left: 193px; top: 40px; font-size: 62px; font-weight: 300; color: var(--white); letter-spacing: -0.5px; }

  .reseller-cta {
    position: absolute; left: 880px; top: 58px; width: 290px; height: 48px; line-height: 45px; text-align: center;
    border: 1.5px solid var(--white); border-radius: 5px; color: var(--white); font-size: 16px; font-weight: 400; text-decoration: none;
  }

  .plan { position: absolute; left: 193px; display: flex; align-items: center; height: 120px; }
  .plan-40 { top: 150px; }
  .plan-50 { top: 295px; }
  .plan-60 { top: 444px; }
  .plan-price {
    width: 295px; font-size: 132px; font-weight: 900; letter-spacing: -2px; line-height: 1;
    background: linear-gradient(var(--white) 45%, var(--price-shade));
    -webkit-background-clip: text; background-clip: text; color: transparent;
    filter: drop-shadow(4px 6px 5px rgba(0,0,0,.35));
  }
  .plan-desc { font-size: 25px; font-weight: 300; color: var(--white); }
  .plan-desc strong { font-weight: 900; }

  .copyright { position: absolute; top: 871px; left: 0; width: 1200px; text-align: center; font-size: 11px; color: var(--footer-text); padding-right: 110px; }
</style>
</head>
<body>
  <nav class="lang-switch">
    <a class="lang-en" href="#">English</a>
    <a class="lang-es" href="#">Español</a>
  </nav>

  <ul class="quick-links">
    <li>&gt; My Account</li>
    <li>&gt; Activate</li>
    <li>&gt; Add PIN</li>
    <li>&gt; Locations</li>
    <li>&gt; Pay Up</li>
    <li>&gt; Dealers</li>
  </ul>

  <header class="brand">
    <div class="brand-name"><span class="brand-dot"></span>uTalkCredits</div>
    <div class="brand-tagline">No Contracts. No Limits.</div>
  </header>

  <div class="carrier-brand"><span class="carrier-mark"></span>Brightwave Cellular</div>

  <nav class="main-nav">
    <a href="#">Home</a><a href="#">Plans</a><a href="#">Shop</a><a href="#">Coverage</a>
    <a href="#">Features</a><a href="#">About US</a><a href="#">Support</a><a href="#">Contact US</a>
  </nav>

  <main class="promo">
    <aside class="sidebar">
      <div class="sidebar-title title-apps">Download APPS</div>
      <a class="app-link app-zphone" href="#">Zphone</a>
      <a class="app-link app-orbix" href="#">Orbix</a>
      <div class="sidebar-title title-follow">Follow US</div>
      <a class="social-link social-chatterloop" href="#">Chatterloop</a>
      <a class="social-link social-peepstream" href="#">Peepstream</a>
    </aside>
    <div class="divider"></div>

    <h1 class="plans-title">Monthly Plans</h1>
    <a class="reseller-cta" href="#">Become a Reseller / Distributor &rsaquo;</a>

    <div class="plan plan-40"><span class="plan-price">$40</span><span class="plan-desc">Unlimited Nationwide Talk &amp; Text</span></div>
    <div class="plan plan-50"><span class="plan-price">$50</span><span class="plan-desc">Unlimited Nationwide Talk &amp; Text + 100Mb of Web</span></div>
    <div class="plan plan-60"><span class="plan-price">$60</span><span class="plan-desc"><strong>Unlimited Everything</strong> Nationwide Talk, Text &amp; Web</span></div>
  </main>

  <footer class="copyright">© 2011 Brightwave Cellular - All rights reserved.</footer>
</body>
</html>
```